MUSIC FESTIVAL 2023

On the occasion of the 2023 music festival, the 24th, brings the VENTOLIRE group to its terrace.
We are organizing a giant barbecue on this occasion.
This event is organized in collaboration with LE MORVAN.
Possibility of take-out!
Address of the event: 12-16 Place Gaston Morlier in CAMBRAI.4
From 19h.
03 41 56 92 17 - lucas@ormeval-gestione.com
Please write in French.
To use the logos of the two establishments.

```html
<!DOCTYPE html>
<html lang="fr">
<head>
<meta charset="UTF-8">
<title>Festival de Musique 2023 — Le Quarante</title>
<link rel="stylesheet" href="https://fonts.googleapis.com/css2?family=Alfa+Slab+One&family=Bebas+Neue&family=Oswald:wght@500;700&family=Roboto+Slab:wght@400;700&display=swap">
<style>
  :root {
    --page-bg: #d9d9d9;
    --paper: #ffffff;
    --night: #0d0b22;
    --stage-red: #8a0f1f;
    --stage-violet: #5a1260;
    --stage-pink: #b0207a;
    --gold: #d9902a;
    --white: #ffffff;
    --ink: #111111;
    --neon-blue: #4b5dff;
    --neon-red: #ff3a1a;
    --address-pink: #ff4fe0;
    --outline-grey: #6d6d78;
  }
  * { margin: 0; padding: 0; box-sizing: border-box; }
  html, body { width: 1006px; height: 1200px; overflow: hidden; background: var(--page-bg); }
  .poster {
    position: absolute; left: 66px; top: 0;
    width: 874px; height: 1200px;
    background: var(--paper);
    overflow: hidden;
    font-family: "Bebas Neue", "Oswald", sans-serif;
  }
  .stage {
    position: absolute; left: 24px; top: 21px; width: 826px; height: 1020px;
    background:
      radial-gradient(ellipse 60% 22% at 50% 8%, rgba(210,30,50,.75), transparent 70%),
      radial-gradient(ellipse 30% 18% at 8% 22%, rgba(200,40,200,.55), transparent 70%),
      radial-gradient(ellipse 70% 25% at 50% 92%, var(--stage-pink), transparent 75%),
      radial-gradient(ellipse 60% 18% at 50% 72%, rgba(120,40,200,.5), transparent 70%),
      linear-gradient(180deg, var(--stage-red) 0%, #2a0b2e 25%, var(--night) 45%, #1a1240 70%, var(--stage-violet) 100%);
  }
  .torn-edge { position: absolute; left: 0; top: 990px; width: 874px; height: 60px; }

  .brand {
    position: absolute; left: 0; top: 120px; width: 874px;
    display: flex; align-items: center; justify-content: center; gap: 14px;
  }
  .brand__dot { width: 22px; height: 22px; border-radius: 50%; background: var(--white); }
  .brand__name { font-family: "Oswald", sans-serif; font-weight: 700; font-size: 52px; color: var(--white); letter-spacing: 2px; }

  .tagline {
    position: absolute; left: 0; width: 874px; text-align: center;
    font-size: 31px; letter-spacing: .3px; color: var(--gold); line-height: 1;
  }
  .tagline em { font-style: normal; color: var(--white); }
  .tagline--top { top: 300px; }
  .tagline--bottom { top: 640px; color: var(--white); }
  .tagline--bottom em { color: var(--gold); }
  .rule { position: absolute; left: 136px; width: 600px; height: 3px; background: var(--gold); }
  .rule--top { top: 340px; }
  .rule--bottom { top: 678px; }

  .title { position: absolute; left: 135px; font-family: "Alfa Slab One", serif; line-height: 1; transform-origin: left top; }
  .title--festival {
    top: 340px; font-size: 92px; letter-spacing: -2px; color: var(--white);
    transform: scaleY(1.75); text-shadow: 4px 3px 0 var(--gold);
  }
  .title--musique {
    top: 500px; font-size: 73px; letter-spacing: 2px; color: var(--white);
    -webkit-text-stroke: 2px var(--outline-grey);
    transform: scaleY(1.55); text-shadow: 3px 3px 0 var(--gold);
  }
  .year {
    position: absolute; left: 672px; top: 492px;
    font-size: 86px; color: var(--gold); line-height: 1;
    transform: rotate(-90deg); transform-origin: left top;
  }

  .neon-sign {
    position: absolute; left: 193px; top: 733px; width: 496px; height: 122px;
    border: 5px solid var(--neon-blue); border-radius: 61px;
    box-shadow: 0 0 14px var(--neon-blue), inset 0 0 14px var(--neon-blue);
    display: flex; align-items: center; justify-content: center;
  }
  .neon-sign__text { font-size: 66px; color: #ffb38a; text-shadow: 0 0 6px var(--neon-red), 0 0 14px var(--neon-red); }

  .address {
    position: absolute; left: 0; top: 884px; width: 874px; text-align: center;
    font-family: "Alfa Slab One", serif; font-size: 22px; line-height: 36px;
    color: var(--address-pink); -webkit-text-stroke: 0.8px var(--white);
  }

  .partner { position: absolute; left: 51px; top: 1082px; font-family: "Oswald", sans-serif; font-weight: 700; font-size: 24px; line-height: 38px; color: var(--ink); }
  .partner-name { position: absolute; left: 313px; top: 1096px; font-family: "Oswald", sans-serif; font-weight: 700; font-size: 34px; color: var(--ink); }
  .divider { position: absolute; left: 504px; top: 1085px; width: 2px; height: 65px; background: var(--ink); }
  .contact__phone { position: absolute; left: 535px; top: 1078px; font-family: "Oswald", sans-serif; font-weight: 700; font-size: 50px; line-height: 1; color: var(--ink); }
  .contact__email { position: absolute; left: 537px; top: 1137px; font-family: "Roboto Slab", serif; font-size: 16px; color: var(--ink); }
</style>
</head>
<body>
  <div class="poster">
    <div class="stage" role="img" aria-label="Scène de concert avec projecteurs rouges et violets, mur de briques et notes de musique"></div>
    <svg class="torn-edge" viewBox="0 0 874 60" preserveAspectRatio="none" aria-hidden="true">
      <polygon fill="#ffffff" points="0,30 30,22 60,34 95,18 130,28 170,14 210,26 250,20 290,36 330,24 370,30 410,16 450,28 490,22 530,34 570,18 610,26 650,20 690,32 730,22 770,30 810,18 850,26 874,22 874,60 0,60"/>
    </svg>

    <div class="brand">
      <span class="brand__dot"></span>
      <span class="brand__name">LE QUARANTE</span>
    </div>

    <p class="tagline tagline--top">FAIT VENIR LE GROUPE <em>VENTOLIRE</em> SUR SA TERRASSE</p>
    <div class="rule rule--top"></div>

    <h1 class="title title--festival">FESTIVAL</h1>
    <div class="year">2023</div>
    <h2 class="title title--musique">DE MUSIQUE</h2>

    <p class="tagline tagline--bottom">ORGANISER UN <em>BARBECUE</em> GÉANT À CETTE OCCASION</p>
    <div class="rule rule--bottom"></div>

    <div class="neon-sign"><span class="neon-sign__text">4 A PARTIR DE 19H</span></div>

    <p class="address">12-16 Place Gaston<br>Morlier à CAMBRAI</p>

    <p class="partner">ÉVÉNEMENT EST ORGANISÉ<br>EN COLLABORATION AVEC</p>
    <p class="partner-name">LE MORVAN</p>
    <div class="divider"></div>
    <p class="contact__phone">03 41 56 92 17</p>
    <p class="contact__email">lucas@ormeval-gestione.com</p>
  </div>
</body>
</html>
```